依頼詳細
基本レイアウトについては
https://zuvaro.com/diagrams/7kq2m94T3XhpleWn
もしくは、添付データのワイヤーをご参照ください。

全体の雰囲気としては
http://www.morelid.co.jp/eco/forest/
のような和風・職人の雰囲気がありつつも、
あまり古臭くならないようなイメージを希望いたします。

色合いについては特に制限はないですが、上記を踏まえ
赤(エンジ)・オレンジ・紫・緑・ベージュなどが良いかと思います。

提出の写真素材があまり多くないのですが、
http://boxquiltry.jp/download/8fa27cd04b91e5a36d0c2bb7105e94f2d6a1c479
にアップロードしたものをご利用いただければ幸いです。

また、
http://vomre.jp/
などから、5000円程度までならこちらにて購入可能です。
カンプデータにて作成頂き、納品時に当方にて購入したデータに差し替えていただければと存じます。

【ロゴについて】
ロゴについては代表の家紋である
「剣片喰 (けんかたばみ)」を使用します。
添付データにjpgのデータを添付しております。
色合いについては、必ずしも黒である必要はないので、デザインに合わせて
ご調整いただいて結構です。

ページ数
1ページ
希望イメージ
シンプル 複雑
単色 カラフル
暗い 明るい
日常 高級
遊び心 厳粛
未来的 伝統的
女性的 男性的
希望する色
特に規定はないですが、和風をイメージを取り入れた色合いを希望します。
納品ファイル
• 高解像度JPG (.jpg)
• フォトショップ形式 (.psd)
補足説明
先方提出のイメージ写真については
下記URLからダウンロードしてご利用ください。

また、
http://vomre.jp/

【参考サイト】
hhttp://www.morelid.co.jp/eco/forest/
→全体の構成、誠実な印象とコンテンツの見やすさを気に入られています。
→色合いについては、必ずしもグリーンベースである必要はありません。

基本的には和風・職人の雰囲気を出すようなサイトが希望なのですが、
あまり和風すぎる、職人すぎる印象は出したくない要望がございます。
(代表自体が35歳と若いこと、マンションの緑地管理などを出していく希望があるため)

http://tokuvane.jp/
のような雰囲気だと、少し古臭すぎる印象がございます。

とはいえ
http://www.qrv-jp.com/
のような感じですと少しポップすぎる印象です

http://plinth-galore.com/2012/166.html
http://plinth-galore.com/2011/115.html
→フッター部分の参照
■ 選んだ理由

クライアントとの協議の結果、こちらの案を採用させて頂きました。
職人っぽい雰囲気でありつつ、今っぽい印象を残したデザインが
選考の決め手になりました。

■ 提案者全員のお礼・コメント

この度は多数ご提案いただきありがとうございました。
当選に至らなかったランサー様には大変心苦しいのですが、
次の機会がございましたら、是非ご提案頂ければ幸いです。
引続きよろしくお願いいたします。

```html
<!DOCTYPE html>
<html lang="ja">
<head>
<meta charset="utf-8">
<title>葉守園</title>
<link href="https://fonts.googleapis.com/css2?family=Noto+Sans+JP:wght@400;700&family=Noto+Serif+JP:wght@500;700&display=swap" rel="stylesheet">
<style>
:root{
  --page:#ececec;
  --ink:#333;
  --header:#1d1914;
  --nav-top:#6f6b3a;
  --nav-bottom:#4d4a24;
  --green:#3f5f26;
  --green-dark:#2f4a1b;
  --green-light:#6d8a3c;
  --orange:#e58c1f;
  --beige:#efe6cc;
  --line:#d9ceb0;
  --footer:#4a3220;
  --footer-dark:#2f1f12;
  --white:#fff;
}
*{box-sizing:border-box;margin:0;padding:0}
html,body{width:874px;height:1200px;overflow:hidden}
body{background:var(--page);font-family:"Noto Sans JP",sans-serif;color:var(--ink);position:relative}
.site{position:absolute;left:88px;top:30px;width:698px;height:1140px;background:var(--white)}
.header{position:absolute;left:0;top:0;width:698px;height:78px;background:var(--header)}
.brand{position:absolute;left:18px;top:20px;display:flex;align-items:center;gap:10px;color:var(--white);font-family:"Noto Serif JP",serif;font-weight:700;font-size:30px;line-height:1.2;letter-spacing:2px}
.brand .mark{width:32px;height:32px;border-radius:50%;background:var(--white)}
.contact{position:absolute;right:14px;top:6px;text-align:right;color:var(--white);line-height:1.3;white-space:nowrap}
.contact .tel{font-size:20px;font-weight:700;letter-spacing:1px;line-height:1.1}
.contact .hours{font-size:8px}
.contact .addr{font-size:11px}
.contact .btns{display:flex;gap:4px;justify-content:flex-end;margin-top:2px}
.btn-small{background:var(--orange);color:var(--white);font-size:8.5px;line-height:1.4;padding:1px 6px}
.nav{position:absolute;left:0;top:78px;width:698px;height:36px;background:linear-gradient(var(--nav-top),var(--nav-bottom));display:flex;align-items:center;justify-content:space-around;padding:0 6px}
.nav a{color:var(--white);font-size:11px;text-decoration:none;white-space:nowrap}
.hero{position:absolute;left:0;top:114px;width:698px;height:258px;background:linear-gradient(160deg,#31402a 0%,#4f6b33 40%,#2c3a22 75%,#6f7560 100%)}
.hero-copy{position:absolute;left:190px;top:34px;color:var(--white);font-family:"Noto Serif JP",serif;font-weight:700;font-size:22px;line-height:1.5;text-shadow:0 1px 3px rgba(0,0,0,.6)}
.hero-list{position:absolute;left:190px;top:118px;color:var(--white);font-weight:700;font-size:17px;line-height:1.55;list-style:none;text-shadow:0 1px 3px rgba(0,0,0,.6)}
.sidebar{position:absolute;left:0;top:380px;width:208px}
.side-proposal{height:110px;background:linear-gradient(var(--green-light),var(--green));color:var(--white);font-family:"Noto Serif JP",serif;font-size:17px;line-height:1.5;padding:32px 12px}
.side-inquiry{margin-top:6px;height:164px;background:linear-gradient(#5d5a44,#39382a);color:var(--white);padding:18px 12px}
.side-inquiry .title{font-family:"Noto Serif JP",serif;font-size:16px;line-height:1.6;white-space:nowrap}
.side-inquiry .tel{font-size:17px;font-weight:700;margin-top:14px}
.side-inquiry .note{font-size:9px;margin-top:4px;opacity:.85}
.side-nav{margin-top:8px;background:var(--green);padding:10px 0;list-style:none}
.side-nav li{color:var(--white);font-size:10px;padding:8px 14px;border-bottom:1px solid var(--green-dark)}
.side-nav li::before{content:"▸ ";color:#c8d89c}
.main{position:absolute;left:222px;top:380px;width:466px}
.news-head{background:var(--beige);font-size:11px;font-weight:700;padding:7px 10px;border-bottom:2px solid var(--line)}
.news{list-style:none;padding:6px 10px 8px}
.news li{font-size:11px;line-height:1.95;border-bottom:1px dotted var(--line)}
.news span{margin-right:10px}
.intro{position:relative;height:232px;margin-top:6px;border-top:1px solid var(--line)}
.intro p{position:absolute;left:8px;top:14px;width:210px;font-size:10px;line-height:1.75}
.intro .photo{position:absolute;left:232px;top:14px;width:226px;height:168px;background:linear-gradient(135deg,#b07a4a,#8d6a48 50%,#c9b08a)}
.intro .more{position:absolute;left:232px;top:192px;background:var(--orange);color:var(--white);font-size:11px;padding:5px 14px}
.works-head{margin-top:4px;font-size:11px;font-weight:700;padding:5px 8px;border-bottom:2px solid var(--green)}
.works{display:flex;gap:14px;margin-top:10px;padding:0 4px}
.work{flex:1}
.work .pair{display:flex;gap:4px}
.work .shot{flex:1;height:150px;background:linear-gradient(150deg,#7d7a6a,#a89b82 60%,#cfc4a8)}
.work .shot.after{background:linear-gradient(150deg,#5a6e40,#8a8c6a 60%,#bcb597)}
.work .cap{font-size:10px;margin-top:5px}
.footer{position:absolute;left:0;top:1012px;width:698px;height:128px;background:var(--footer);color:var(--white)}
.footer-links{display:flex;gap:7px;font-size:8.5px;padding:9px 10px;white-space:nowrap}
.footer .brand{top:52px}
.footer .contact{top:34px}
.copyright{position:absolute;left:0;bottom:0;width:698px;height:24px;background:var(--footer-dark);font-size:9px;text-align:center;line-height:24px}
</style>
</head>
<body>
<div class="site">
  <header class="header">
    <div class="brand"><span class="mark"></span>葉守園</div>
    <div class="contact">
      <div class="tel">TEL:0120-314-862</div>
      <div class="hours">受付時間 9:00〜18:00</div>
      <div class="addr">川崎市中原区若葉台3-2-8</div>
      <div class="btns"><span class="btn-small">資料請求</span><span class="btn-small">お見積り・お問い合わせはこちら</span></div>
    </div>
  </header>
  <nav class="nav">
    <a>トップページ</a><a>植木屋の仕事について</a><a>造園・外構工事</a><a>マンション緑地管理</a><a>施工実績</a><a>よくある質問</a><a>会社案内</a>
  </nav>
  <section class="hero" role="img" aria-label="苔と刈り込まれた植木が並ぶ日本庭園の写真">
    <h1 class="hero-copy">お庭のことなら、<br>どんなことでもお気軽にご相談ください</h1>
    <ul class="hero-list"><li>●植木屋の仕事</li><li>●造園、外構工事</li><li>●マンションの緑地管理</li></ul>
  </section>
  <aside class="sidebar">
    <div class="side-proposal">マンション緑地管理の<br>ご提案</div>
    <div class="side-inquiry">
      <div class="title">資料請求・<br>お問い合わせはこちら</div>
      <div class="tel">TEL:0120-314-862</div>
      <div class="note">受付時間 平日9:00〜18:00</div>
    </div>
    <ul class="side-nav">
      <li>トップページ</li><li>植木屋の仕事について</li><li>造園・外構工事</li><li>マンション緑地管理</li><li>施工実績</li><li>よくある質問</li><li>会社案内</li><li>お問い合わせ</li>
    </ul>
  </aside>
  <main class="main">
    <div class="news-head">新着情報</div>
    <ul class="news">
      <li><span>2013年5月20日</span>茅ヶ崎A邸　外構工事</li>
      <li><span>2013年4月26日</span>川崎T邸　造園工事</li>
      <li><span>2013年5月21日</span>横浜マンション緑地管理</li>
    </ul>
    <div class="intro">
      <p>植木の剪定から庭づくり、門まわりの外構工事まで、職人が一つひとつ丁寧に仕上げます。ブロック塀、フェンス、カーポート等の工事もお任せください。<br>マンションの植栽管理も承っております。年間を通じた緑地の手入れをご提案いたします。<br>お見積りは無料です。お気軽にご相談ください。</p>
      <div class="photo" role="img" aria-label="庭で作業をする職人の写真"></div>
      <span class="more">詳しくはこちら</span>
    </div>
    <div class="works-head">施工事例</div>
    <div class="works">
      <div class="work">
        <div class="pair">
          <div class="shot" role="img" aria-label="施工前の庭の写真"></div>
          <div class="shot after" role="img" aria-label="施工後の庭の写真"></div>
        </div>
        <div class="cap">川崎K邸　ビフォーアフター</div>
      </div>
      <div class="work">
        <div class="pair">
          <div class="shot" role="img" aria-label="施工前の通路の写真"></div>
          <div class="shot after" role="img" aria-label="施工後の通路の写真"></div>
        </div>
        <div class="cap">横浜T邸　ビフォーアフター</div>
      </div>
    </div>
  </main>
  <footer class="footer">
    <div class="footer-links"><span>トップページ</span><span>植木屋の仕事について</span><span>造園・外構工事</span><span>マンション緑地管理</span><span>施工実績</span><span>よくある質問</span><span>会社案内</span><span>サイトマップ</span><span>プライバシーポリシー</span><span>お問い合わせ</span></div>
    <div class="brand"><span class="mark"></span>葉守園</div>
    <div class="contact">
      <div class="tel">TEL:0120-314-862</div>
      <div class="hours">受付時間 9:00〜18:00</div>
      <div class="addr">川崎市中原区若葉台3-2-8</div>
      <div class="btns"><span class="btn-small">お見積り・お問い合わせはこちら</span></div>
    </div>
    <div class="copyright">Copyright © 2013 葉守園 All Rights Reserved.</div>
  </footer>
</div>
</body>
</html>
```